bookcover Lantern Orchard

I need a book cover suitable for both an ereader and a 6" X 9" paperback. I would want the font to be the same as the sample text attached in a screenshot of the TITLE PAGE LANTERN ORCHARD (or very similar). The font is PT Sans. Text one and Text two for the back cover is from PAGES and will need to be converted to the font used on the front cover. Text One paragraph is a book description. Text Two paragraph is a review. They should be separate. Two Pixfold images -1) The brain of multiple colored wires goes on the front page. 2) The green neurons likely on the back. Logo is for the spine (several versions attached).

```html
<!DOCTYPE html>
<html lang="en">
<head>
<meta charset="utf-8">
<title>Lantern Orchard — Book Cover</title>
<link href="https://fonts.googleapis.com/css2?family=PT+Sans:ital,wght@0,400;0,700;1,400&family=PT+Sans+Narrow:wght@400;700&display=swap" rel="stylesheet">
<style>
  :root {
    --stage: #e9e7e4;
    --paper-light: #fbfbfb;
    --paper-mid: #eeeeee;
    --ink: #2b2b2b;
    --ink-soft: #444444;
    --rule: #6f9a86;
    --subtitle-ink: #2f5147;
    --accent-green: #5aa64a;
  }
  * { box-sizing: border-box; margin: 0; padding: 0; }
  html, body {
    width: 1200px; height: 788px; overflow: hidden;
    background: var(--stage);
    font-family: "PT Sans", sans-serif;
    color: var(--ink);
  }
  .wrap-cover {
    position: absolute; left: 65px; top: 24px;
    width: 1070px; height: 740px;
    display: flex;
    box-shadow: 0 4px 18px rgba(0,0,0,.18);
  }
  .panel {
    height: 100%;
    background: linear-gradient(135deg, var(--paper-light) 0%, var(--paper-mid) 100%);
    position: relative;
  }
  /* Back cover */
  .back { width: 500px; padding: 44px 46px 36px; }
  .back-title {
    font-family: "PT Sans Narrow", sans-serif; font-weight: 700;
    font-size: 30px; text-align: center; letter-spacing: 1px;
  }
  .back-subtitle {
    font-size: 17px; font-weight: 700; text-align: center; margin: 4px 0 16px;
  }
  .back p, .back li { font-size: 14px; line-height: 1.45; color: var(--ink-soft); }
  .back p { margin-bottom: 12px; }
  .back ul { margin: 0 0 14px 18px; }
  .back li { font-weight: 700; margin-bottom: 4px; }
  .back-art {
    position: absolute; left: 120px; top: 320px; width: 260px; height: 190px;
    border-radius: 50%;
    background: radial-gradient(ellipse, rgba(120,190,90,.22), rgba(120,190,90,0) 70%);
  }
  .back-text { position: relative; }
  .review { font-style: italic; }
  .reviewer { font-weight: 700; margin-top: 16px; font-size: 14px; }
  .reviewer-bio { font-size: 13px; color: var(--ink-soft); line-height: 1.4; }

  /* Spine */
  .spine {
    width: 70px;
    border-left: 1px solid #d6d6d6; border-right: 1px solid #d6d6d6;
    display: flex; flex-direction: column; align-items: center;
    padding: 26px 0 18px;
  }
  .spine-title {
    writing-mode: vertical-rl;
    font-family: "PT Sans Narrow", sans-serif;
    font-size: 38px; letter-spacing: 1px; line-height: 1;
  }
  .spine-art {
    width: 46px; height: 40px; margin: 18px 0; border-radius: 50%;
    background: radial-gradient(circle, #e94b6a 0%, #f0a23a 40%, #3fa0d8 75%, #f6f6f6 100%);
  }
  .spine-author {
    writing-mode: vertical-rl;
    font-weight: 700; font-size: 20px; letter-spacing: 1px; line-height: 1.1;
  }
  .spine-role {
    writing-mode: vertical-rl;
    font-size: 12px; letter-spacing: 1px; margin-top: 4px;
  }
  .spine-publisher {
    margin-top: auto; display: flex; flex-direction: column; align-items: center; gap: 4px;
    font-size: 11px; font-weight: 700;
  }
  .publisher-dot { width: 18px; height: 18px; border-radius: 50%; background: var(--accent-green); }

  /* Front cover */
  .front { width: 500px; padding: 58px 40px 40px; text-align: center; }
  .front-title {
    font-family: "PT Sans Narrow", sans-serif; font-weight: 400;
    font-size: 96px; line-height: .92; letter-spacing: 2px; color: #1f1f1f;
  }
  .front-subtitle {
    margin: 18px auto 0; width: 400px;
    border-top: 2px solid var(--rule); border-bottom: 2px solid var(--rule);
    padding: 8px 0;
    font-family: "PT Sans Narrow", sans-serif;
    font-size: 22px; line-height: 1.1; color: var(--subtitle-ink); letter-spacing: .5px;
  }
  .front-art {
    margin: 26px auto 0; width: 300px; height: 270px; border-radius: 46% 46% 40% 40%;
    background: radial-gradient(circle at 30% 40%, #e8405f 0%, rgba(232,64,95,0) 45%),
                radial-gradient(circle at 70% 35%, #2f9ad6 0%, rgba(47,154,214,0) 45%),
                radial-gradient(circle at 50% 70%, #f2b035 0%, rgba(242,176,53,0) 50%),
                radial-gradient(circle at 45% 45%, #7bbf45 0%, #f4f4f4 80%);
  }
  .front-author { margin-top: 40px; font-weight: 700; font-size: 38px; letter-spacing: 1px; }
  .front-role { font-size: 20px; letter-spacing: 2px; color: var(--ink-soft); }
</style>
</head>
<body>
  <div class="wrap-cover">
    <section class="panel back">
      <div class="back-art" role="img" aria-label="Faint illustration of green neurons"></div>
      <div class="back-text">
        <h2 class="back-title">LANTERN ORCHARD</h2>
        <div class="back-subtitle">Resetting the mind to ease stress and restore calm</div>
        <p>Every day, countless people carry a quiet load of tension that colors how they rest, learn and connect. This book explains why an overworked nervous system struggles to settle, and what can be done to help it find balance again.</p>
        <ul>
          <li>Learn how lasting tension shapes mood and focus.</li>
          <li>Explore a calm, drug-free method for guiding the mind back to rest.</li>
          <li>Track progress with simple, measurable signs.</li>
          <li>Spot early warning signals before they grow.</li>
        </ul>
        <p>Drawing on decades of practice with children and families, the author offers warm, clear steps that readers can begin using at home, at school and in the clinic, one small change at a time.</p>
        <p class="review">A hopeful and deeply useful guide. Vale writes with rare clarity, turning careful science into gentle, everyday tools that parents and caregivers can trust.</p>
        <div class="reviewer">Dr. E. K. Holloway</div>
        <div class="reviewer-bio">Dr. Holloway is a family counselor, lecturer and author of several books on childhood wellbeing.</div>
      </div>
    </section>

    <section class="panel spine">
      <div class="spine-title">LANTERN ORCHARD</div>
      <div class="spine-art" role="img" aria-label="Small multicoloured wire brain illustration"></div>
      <div class="spine-author">MARIAN T. VALE</div>
      <div class="spine-role">PSYCHOLOGIST</div>
      <div class="spine-publisher"><span class="publisher-dot"></span>Fernleaf</div>
    </section>

    <section class="panel front">
      <h1 class="front-title">LANTERN<br>ORCHARD</h1>
      <div class="front-subtitle">RESETTING the MIND to EASE STRESS<br>and RESTORE CALM</div>
      <div class="front-art" role="img" aria-label="Brain made of multicoloured tangled wires ending in a plug"></div>
      <div class="front-author">MARIAN T. VALE</div>
      <div class="front-role">PSYCHOLOGIST</div>
    </section>
  </div>
</body>
</html>
```